Project Title:
Dental Implant Overdenture Flyer (Retirement Village Target)
Objective:
Create a clean, trustworthy, and reassuring flyer aimed at older adults (60–85 years old) who struggle with loose dentures. The goal is to educate them about implant-retained “clip-on” dentures and encourage them to book a consultation.
Tone & Feel:
Warm, caring, non-intimidating
Premium but not “salesy”
Medical but easy to understand
Focus on improving quality of life (confidence, eating, comfort)
Target Audience:
Retirees / pensioners
Existing denture wearers
People frustrated with loose or uncomfortable dentures
Key Message:
“You don’t have to live with loose dentures anymore.”
Design Style:
Clean, minimal, modern
Soft colours (blues, greens, warm neutrals)
Easy-to-read large font
High contrast for older eyes
Avoid clutter
Imagery Suggestions:
Smiling older adults (natural, not stocky/overly staged)
Before/after lifestyle (eating, laughing, socialising)
Simple diagram showing denture clipping onto implants
Avoid graphic surgical images
Layout Suggestions:
A5 or DL flyer
Clear sections with headings
Icons for benefits
Strong call-to-action at bottom
HEADLINE (big and bold)
Tired of Loose Dentures?
Discover Secure “Clip-On” Teeth
🔹 PROBLEM SECTION
Do your dentures:
Slip or move when eating?
Make it hard to chew certain foods?
Feel uncomfortable or loose?
Affect your confidence when speaking or smiling?
You’re not alone — and there is a better solution.
🔹 SOLUTION SECTION
Implant-Retained “Clip-On” Dentures
We can secure your denture using just 2 dental implants, allowing your teeth to:
✔ Stay firmly in place
✔ Improve your ability to eat
✔ Feel more comfortable
✔ Boost your confidence
🔹 SIMPLE EXPLANATION (very important)
Small titanium implants are gently placed in the jaw.
Your denture then clips securely onto them, stopping movement.
🔹 PRICE SECTION (highlight this clearly)
$12,000
Includes:
2 dental implants
A brand new custom overdenture
Does not include sedation or extractions (if needed)
🔹 SEDATION
Sedation is available for comfort.
If you hold a pensioner card, you may receive a significant Vantacor rebate, often resulting in minimal out-of-pocket costs for sedation.
🔹 TRUST / REASSURANCE
Experienced implant clinician
Gentle, patient-focused care
Modern technology and techniques
🔹 CALL TO ACTION (VERY IMPORTANT)
Book a Free Consultation
📞 Call: 08 9351 4276
🌐 Visit: www.bravonclinic.com.au
📍 Located near Tallowmere shopping centre
🔹 OPTIONAL TAGLINE
Eat Better. Feel Better. Smile with Confidence Again.
Please include some photos to illustrate what a clip on denture looks like with two implants.

```html
<!DOCTYPE html>
<html lang="en">
<head>
<meta charset="utf-8">
<title>Bravon Clinic – Clip-On Dentures Flyer</title>
<link href="https://fonts.googleapis.com/css2?family=Anton&family=Montserrat:wght@400;500;600;700;800&display=swap" rel="stylesheet">
<style>
:root{
  --teal:#4bbfba;
  --teal-deep:#2a96b0;
  --cyan:#36c2d6;
  --navy:#1c3640;
  --green:#5fd3a6;
  --ink:#2b3a40;
  --paper:#ffffff;
  --mist:#eef1f3;
  --bg:#eceeee;
}
*{box-sizing:border-box;margin:0;padding:0}
html,body{width:1200px;height:3378px;overflow:hidden}
body{background:var(--bg);font-family:"Montserrat",sans-serif;color:var(--ink);position:relative}
.page{position:absolute;left:40px;width:1120px;height:1584px;background:var(--paper);overflow:hidden}
.page--front{top:70px}
.page--back{top:1724px}
.abs{position:absolute}

/* front */
.brand{left:108px;top:70px;display:flex;align-items:center;gap:18px}
.brand__dot{width:26px;height:26px;border-radius:50%;background:var(--teal-deep)}
.brand__name{font-weight:700;font-size:34px;letter-spacing:6px;color:var(--teal-deep)}
.hero-photo{right:0;top:0;width:560px;height:606px;border-radius:0 0 0 300px;
  background:linear-gradient(135deg,#d9d2c8 0%,#e9ddd0 40%,#9fa8ae 100%)}
.hero-band{left:0;top:206px;width:660px;height:236px;background:var(--teal)}
.hero-title{left:64px;top:222px;font-family:"Anton",sans-serif;font-size:96px;line-height:98px;color:#fff;text-transform:uppercase}
.hero-strip{left:0;top:442px;width:660px;height:58px;background:var(--teal-deep);color:#fff;font-weight:800;font-size:31px;line-height:58px;padding-left:46px}
.hero-sub{left:0;top:500px;width:700px;height:66px;background:var(--teal);color:#e9fbfa;font-size:22px;line-height:66px;padding-left:46px}

.problem{left:36px;top:590px;width:1052px;height:376px;border:4px solid var(--teal-deep);border-radius:10px 10px 0 0}
.problem__title{left:40px;top:36px;font-weight:700;font-size:40px;color:var(--teal)}
.problem__list{left:40px;top:100px;width:420px;list-style:none}
.problem__list li{position:relative;padding-left:44px;font-size:23px;line-height:28px;margin-bottom:14px;font-weight:500}
.problem__list li::before{content:"×";position:absolute;left:0;top:3px;width:22px;height:22px;border-radius:50%;background:var(--teal);color:#fff;font-size:18px;line-height:20px;text-align:center;font-weight:700}
.shot{top:18px;width:256px;height:294px}
.shot__img{width:100%;height:254px}
.shot__label{height:40px;line-height:40px;text-align:center;color:#fff;font-weight:700;font-size:21px}
.shot--before{left:480px}
.shot--before .shot__img{background:linear-gradient(160deg,#c9bfb5,#8f8a86)}
.shot--before .shot__label{background:#9ba3a7}
.shot--after{left:754px}
.shot--after .shot__img{background:linear-gradient(160deg,#e2d5c6,#b4a391)}
.shot--after .shot__label{background:var(--teal)}
.problem__bar{left:-4px;bottom:-4px;width:1052px;height:52px;background:var(--teal-deep);color:#fff;font-weight:600;font-size:27px;line-height:52px;text-align:center}

.solution-top{left:0;top:992px;width:1120px;height:214px;background:var(--teal-deep)}
.solution-bottom{left:0;top:1206px;width:1120px;height:250px;background:var(--teal)}
.solution-title{left:80px;top:1020px;color:#fff;font-weight:700;font-size:46px;line-height:50px}
.solution-text{left:80px;top:1126px;color:#e6f6fa;font-size:23px;line-height:26px}
.benefits{left:80px;top:1232px;list-style:none}
.benefits li{position:relative;padding-left:50px;color:#fff;font-weight:600;font-size:26px;line-height:52px}
.benefits li svg{position:absolute;left:0;top:13px}

.price{left:628px;top:1016px;width:426px;height:410px;background:#fff;border:4px solid #fff;box-shadow:0 0 0 4px var(--teal-deep) inset}
.price__amount{left:0;top:18px;width:100%;text-align:center;font-weight:700;font-size:94px;color:var(--teal-deep)}
.price__includes{left:8px;top:146px;width:402px;height:164px;background:var(--teal-deep);list-style:none;padding:20px 20px 0 24px}
.price__includes li{position:relative;padding-left:44px;color:#fff;font-size:27px;line-height:28px;margin-bottom:14px}
.price__includes li svg{position:absolute;left:0;top:3px}
.price__note{left:8px;top:310px;width:402px;height:88px;background:var(--cyan);color:#fff;font-size:23px;line-height:26px;padding:18px 0 0 40px;font-weight:500}

.footer-bar{left:0;top:1456px;width:1120px;height:128px;background:var(--navy);display:flex;align-items:center;gap:110px;padding-left:88px;color:#fff;font-weight:600;font-size:35px}
.contact{display:flex;align-items:center;gap:18px}

/* back */
.how-title{left:0;top:62px;width:100%;text-align:center;font-weight:700;font-size:50px;color:var(--teal-deep)}
.step{top:146px;width:296px;height:390px;border:3px solid var(--teal-deep)}
.step--1{left:102px}.step--2{left:414px}.step--3{left:726px}
.step__num{left:-3px;top:-3px;width:62px;height:62px;background:var(--teal-deep);border-radius:0 0 30px 0;color:#fff;font-weight:700;font-size:32px;line-height:58px;padding-left:18px}
.step__img{left:40px;top:74px;width:210px;height:180px;border-radius:40px 40px 80px 80px;background:radial-gradient(circle at 50% 45%,#f6d3d3,#e59d9f 70%,#d88c8e)}
.step__caption{left:0;bottom:0;width:100%;height:128px;background:var(--teal-deep);color:#fff;font-size:19px;line-height:21px;text-align:center;padding:34px 14px 0;font-weight:500}

.trust{left:0;top:590px;width:1120px;height:272px;background:var(--teal);display:flex}
.trust__item{flex:1;display:flex;flex-direction:column;align-items:center;padding-top:42px;color:#fff;font-weight:500;font-size:26px;line-height:28px;text-align:center;position:relative}
.trust__item + .trust__item::before{content:"";position:absolute;left:0;top:52px;height:170px;border-left:2px solid rgba(255,255,255,.7)}
.trust__icon{width:96px;height:96px;border-radius:22px;background:rgba(255,255,255,.22);margin-bottom:24px}

.sedation{left:70px;top:962px;width:996px;height:234px;background:var(--mist);border-radius:18px}
.sedation__art{left:0;top:0;width:330px;height:234px;border-radius:18px 0 0 18px;background:linear-gradient(135deg,#dde3e7,#b9c9d0)}
.sedation__arc{left:300px;top:0;width:60px;height:234px;border-right:5px solid var(--teal-deep);border-radius:0 120px 120px 0}
.sedation__title{left:390px;top:46px;font-weight:700;font-size:42px;line-height:46px;color:var(--teal)}
.sedation__text{left:390px;top:152px;width:560px;font-size:19px;line-height:20px}

.cta{left:0;top:1240px;width:1120px;height:262px;background:var(--navy);color:#fff}
.cta__title{left:0;top:28px;width:100%;text-align:center;font-weight:800;font-size:58px}
.cta__title em{font-style:normal;color:var(--green)}
.cta__contacts{left:110px;top:140px;font-size:30px;font-weight:600;line-height:48px}
.cta__divider{left:558px;top:146px;height:92px;border-left:2px solid rgba(255,255,255,.6)}
.cta__loc{left:590px;top:136px;font-size:30px;font-weight:600;line-height:30px;display:flex;gap:16px}
.tagline{left:0;top:1502px;width:100%;height:82px;text-align:center;line-height:82px;font-size:30px;font-weight:600;color:var(--navy)}
.tagline span{color:var(--teal)}
</style>
</head>
<body>

<section class="page page--front">
  <div class="abs brand"><span class="brand__dot"></span><span class="brand__name">BRAVON CLINIC</span></div>
  <div class="abs hero-photo" role="img" aria-label="Photo of a smiling senior couple laughing together"></div>
  <div class="abs hero-band"></div>
  <h1 class="abs hero-title">Tired of loose<br>dentures?</h1>
  <div class="abs hero-strip">DISCOVER SECURE CLIP-ON TEETH</div>
  <div class="abs hero-sub">You don't have to live with loose dentures anymore</div>

  <div class="abs problem">
    <h2 class="abs problem__title">DO YOUR DENTURES</h2>
    <ul class="abs problem__list">
      <li>Slip or move when eating?</li>
      <li>Feel uncomfortable or loose?</li>
      <li>Make it hard to chew certain foods?</li>
      <li>Affect your confidence when speaking or smiling?</li>
    </ul>
    <figure class="abs shot shot--before">
      <div class="shot__img" role="img" aria-label="Photo of an older woman looking uncomfortable with loose dentures"></div>
      <figcaption class="shot__label">BEFORE</figcaption>
    </figure>
    <figure class="abs shot shot--after">
      <div class="shot__img" role="img" aria-label="Photo of the same woman happily biting into an apple"></div>
      <figcaption class="shot__label">AFTER</figcaption>
    </figure>
    <div class="abs problem__bar">You're not alone and there is a better solution</div>
  </div>

  <div class="abs solution-top"></div>
  <div class="abs solution-bottom"></div>
  <h2 class="abs solution-title">IMPLANT-RETAINED<br>CLIP-ON DENTURES</h2>
  <p class="abs solution-text">We can secure your denture using just<br>2 dental implants, allowing your teeth to</p>
  <ul class="abs benefits">
    <li><svg width="28" height="28" viewBox="0 0 28 28"><circle cx="14" cy="14" r="13" fill="#fff"/><path d="M8 14.5l4 4 8-8" stroke="#4bbfba" stroke-width="3" fill="none"/></svg>Stay firmly in place</li>
    <li><svg width="28" height="28" viewBox="0 0 28 28"><circle cx="14" cy="14" r="13" fill="#fff"/><path d="M8 14.5l4 4 8-8" stroke="#4bbfba" stroke-width="3" fill="none"/></svg>Feel more comfortable</li>
    <li><svg width="28" height="28" viewBox="0 0 28 28"><circle cx="14" cy="14" r="13" fill="#fff"/><path d="M8 14.5l4 4 8-8" stroke="#4bbfba" stroke-width="3" fill="none"/></svg>Improve your ability to eat</li>
    <li><svg width="28" height="28" viewBox="0 0 28 28"><circle cx="14" cy="14" r="13" fill="#fff"/><path d="M8 14.5l4 4 8-8" stroke="#4bbfba" stroke-width="3" fill="none"/></svg>Boost your confidence</li>
  </ul>

  <div class="abs price">
    <div class="abs price__amount">$12,000</div>
    <ul class="abs price__includes">
      <li><svg width="26" height="26" viewBox="0 0 26 26"><circle cx="13" cy="13" r="12" fill="#fff"/><path d="M8 13h9M13 9l4 4-4 4" stroke="#2a96b0" stroke-width="2.5" fill="none"/></svg>2 dental implants</li>
      <li><svg width="26" height="26" viewBox="0 0 26 26"><circle cx="13" cy="13" r="12" fill="#fff"/><path d="M8 13h9M13 9l4 4-4 4" stroke="#2a96b0" stroke-width="2.5" fill="none"/></svg>A brand new custom overdenture</li>
    </ul>
    <div class="abs price__note">Does not include sedation<br>or extractions (if needed)</div>
  </div>

  <div class="abs footer-bar">
    <span class="contact"><svg width="36" height="36" viewBox="0 0 36 36"><circle cx="18" cy="18" r="17" fill="#fff"/><path d="M12 10c-2 2-1 6 3 10s8 5 10 3l1-2-4-3-2 2c-2-1-4-3-5-5l2-2-3-4z" fill="#1c3640"/></svg>08 9351 4276</span>
    <span class="contact"><svg width="36" height="36" viewBox="0 0 36 36"><circle cx="18" cy="18" r="16" fill="#fff"/><g stroke="#1c3640" stroke-width="2" fill="none"><circle cx="18" cy="18" r="10"/><ellipse cx="18" cy="18" rx="4.5" ry="10"/><path d="M8 18h20M10 13h16M10 23h16"/></g></svg>www.bravonclinic.com.au</span>
  </div>
</section>

<section class="page page--back">
  <h2 class="abs how-title">HOW "CLIP-ON" DENTURES WORK</h2>
  <div class="abs step step--1">
    <div class="abs step__img" role="img" aria-label="Illustration of a lower jaw with two titanium implants"></div>
    <div class="abs step__num">1</div>
    <p class="abs step__caption">Small titanium implants are gently placed in the jaw</p>
  </div>
  <div class="abs step step--2">
    <div class="abs step__img" role="img" aria-label="Illustration of a denture lowering onto two implants"></div>
    <div class="abs step__num">2</div>
    <p class="abs step__caption">Your denture then clips securely onto them, stopping movement</p>
  </div>
  <div class="abs step step--3">
    <div class="abs step__img" role="img" aria-label="Illustration of a denture clipped onto the implants"></div>
    <div class="abs step__num">3</div>
    <p class="abs step__caption">The denture clips securely onto the implants, stopping movement</p>
  </div>

  <div class="abs trust">
    <div class="trust__item"><div class="trust__icon" role="img" aria-label="Clinician icon"></div>Experienced<br>implant clinician</div>
    <div class="trust__item"><div class="trust__icon" role="img" aria-label="Caring hands icon"></div>Gentle,patient<br>focused care</div>
    <div class="trust__item"><div class="trust__icon" role="img" aria-label="Digital tooth icon"></div>Modern technology<br>and techniques</div>
  </div>

  <div class="abs sedation">
    <div class="abs sedation__art" role="img" aria-label="Illustration of a relaxed patient in a dental chair with a clinician"></div>
    <div class="abs sedation__arc"></div>
    <h3 class="abs sedation__title">SEDATION IS AVAILABLE<br>FOR COMFORT</h3>
    <p class="abs sedation__text">If you hold a pensioner card, you may receive a significant Vantacor rebate, often resulting in minimal out-of-pocket costs for sedation</p>
  </div>

  <div class="abs cta">
    <h2 class="abs cta__title">BOOK A <em>FREE</em> CONSULTATION</h2>
    <div class="abs cta__contacts">
      <div class="contact"><svg width="30" height="30" viewBox="0 0 36 36"><circle cx="18" cy="18" r="17" fill="#fff"/><path d="M12 10c-2 2-1 6 3 10s8 5 10 3l1-2-4-3-2 2c-2-1-4-3-5-5l2-2-3-4z" fill="#1c3640"/></svg>08 9351 4276</div>
      <div class="contact"><svg width="30" height="30" viewBox="0 0 36 36"><circle cx="18" cy="18" r="16" fill="#fff"/><g stroke="#1c3640" stroke-width="2" fill="none"><circle cx="18" cy="18" r="10"/><ellipse cx="18" cy="18" rx="4.5" ry="10"/><path d="M8 18h20M10 13h16M10 23h16"/></g></svg>www.bravonclinic.com.au</div>
    </div>
    <div class="abs cta__divider"></div>
    <div class="abs cta__loc"><svg width="30" height="30" viewBox="0 0 30 30"><circle cx="15" cy="15" r="14" fill="#fff"/><path d="M15 7a5.5 5.5 0 0 0-5.5 5.5c0 4 5.5 10 5.5 10s5.5-6 5.5-10A5.5 5.5 0 0 0 15 7z" fill="#1c3640"/><circle cx="15" cy="12.5" r="2" fill="#fff"/></svg><span>Located near<br>Tallowmere<br>shopping centre</span></div>
  </div>
  <p class="abs tagline"><span>Eat Better. Feel Better.</span> Smile with Confidence Again.</p>
</section>

</body>
</html>
```